Curriculum Card Design for Martial Arts System

We need an editable curriculum card design for a martial arts system. Would like to have our logo in background or highlighted on card. Each level will have their own separate card that can be printed onto a postcard sized paper (5x7 and 6x9). Each technique has three parts to it E, F, and S and would like them to be able to have a line or box which an instructor can initial or check next to each technique. Would like to have each curriculum card be straightforward with slight modern and futuristic touches similar to the emblem and logo.

Industry/Entity Type

Martial Art

Requirements
Must have
• Must be able to be edited as the curriculum techniques and moves may change or added/subracted.We are looking for something that is very easy to understand but also eye catching.
Should not have
• please Don't be boring in design.

```html
<!DOCTYPE html>
<html lang="en">
<head>
<meta charset="utf-8">
<title>Curriculum Card – Ascend Combat Arts</title>
<link href="https://fonts.googleapis.com/css2?family=Anton&family=Alfa+Slab+One&family=Lato:wght@400;700&display=swap" rel="stylesheet">
<style>
:root{
  --page:#e6e8e8;
  --card:#2b7c7c;
  --card-deep:#1f6567;
  --panel:#22696b;
  --band:#1a5658;
  --band-light:#2d7476;
  --ink:#0f2f31;
  --line:#102b2c;
  --text:#eef6f6;
  --accent:#3fd6dc;
  --ribbon:#3b1716;
  --silhouette:#0c1a1b;
}
*{box-sizing:border-box;margin:0;padding:0}
html,body{width:922px;height:1200px;overflow:hidden;background:var(--page)}
.card{
  position:absolute;left:74px;top:20px;width:774px;height:1160px;
  background:radial-gradient(ellipse at 75% 20%,#338888 0%,var(--card) 45%,var(--card-deep) 100%);
  box-shadow:0 4px 14px rgba(0,0,0,.35);
  font-family:'Lato',sans-serif;color:var(--text);overflow:hidden;
}
.side-panel{position:absolute;left:0;top:0;width:278px;height:100%;background:var(--panel)}
.side-band{position:absolute;top:0;height:100%}
.side-band.dark{left:199px;width:30px;background:var(--band)}
.side-band.light{left:238px;width:14px;background:var(--band-light)}
.divider{position:absolute;left:276px;top:0;width:3px;height:100%;background:var(--line)}
.brand-box{
  position:absolute;left:27px;top:22px;width:209px;height:210px;
  border:4px solid var(--ink);background:rgba(15,47,49,.25);
  display:flex;flex-direction:column;align-items:center;justify-content:center;gap:14px;
}
.brand-dot{width:70px;height:70px;border-radius:50%;background:var(--ink)}
.brand-name{font-family:'Lato',sans-serif;font-weight:700;color:var(--accent);font-size:17px;letter-spacing:3px;text-align:center;line-height:1.3;text-transform:uppercase}
.select-label{position:absolute;left:27px;top:282px;font-weight:700;font-size:20px}
.check-row{position:absolute;left:27px;display:flex;align-items:center}
.check-row span{width:30px;color:var(--accent);font-size:20px}
.check-row i{display:block;width:103px;height:27px;border:1px solid var(--accent)}
.figure-art{position:absolute;left:4px;top:428px;width:274px;height:727px;
  background:linear-gradient(180deg,rgba(12,26,27,0) 0%,rgba(12,26,27,.75) 25%,var(--silhouette) 60%,rgba(12,26,27,.85) 100%)}
.frame-top,.frame-bottom{position:absolute;left:305px;width:442px;height:2px;background:var(--line)}
.frame-top{top:28px}.frame-bottom{top:1133px}
.frame-right{position:absolute;left:746px;top:28px;width:2px;height:1107px;background:var(--line)}
.ribbon{position:absolute;width:252px;height:49px}
.ribbon text{font-family:'Alfa Slab One',serif;font-size:27px;fill:#f4f4f4;letter-spacing:1px}
.heading{position:absolute;font-family:'Anton',sans-serif;font-weight:400;font-size:24px;letter-spacing:1.5px;display:flex;align-items:center;gap:6px;white-space:nowrap;line-height:1}
.heading svg{width:14px;height:16px;fill:var(--text);flex:none}
.list{position:absolute;list-style:none;font-size:17px;line-height:28.7px;white-space:nowrap}
.list li::before{content:"•";margin-right:6px}
.rule{position:absolute;width:2px;background:var(--text)}
</style>
</head>
<body>
<main class="card">
  <aside class="side-panel">
    <div class="side-band dark"></div>
    <div class="side-band light"></div>
    <div class="brand-box">
      <div class="brand-dot"></div>
      <div class="brand-name">Ascend<br>Combat Arts</div>
    </div>
    <div class="select-label">SELECT</div>
    <div class="check-row" style="top:315px"><span>E</span><i></i></div>
    <div class="check-row" style="top:357px"><span>F</span><i></i></div>
    <div class="check-row" style="top:403px"><span>S</span><i></i></div>
    <div class="figure-art" role="img" aria-label="Silhouette of a martial artist holding a high standing kick"></div>
  </aside>
  <div class="divider"></div>

  <div class="frame-top"></div><div class="frame-right"></div><div class="frame-bottom"></div>

  <svg class="ribbon" style="left:398px;top:37px" viewBox="0 0 252 49">
    <polygon points="0,0 252,0 232,24.5 252,49 0,49 20,24.5" fill="var(--ribbon)"/>
    <polygon points="6,4 246,4 228,24.5 246,45 6,45 24,24.5" fill="none" stroke="#d9c9c6" stroke-width="1" stroke-dasharray="3 2"/>
    <text x="126" y="35" text-anchor="middle">LEVEL ONE</text>
  </svg>

  <section class="level-one">
    <h2 class="heading" style="left:300px;top:113px"><svg viewBox="0 0 16 18"><polygon points="8,0 15,9 8,18 1,9"/></svg>CONCEPT</h2>
    <ul class="list" style="left:322px;top:148px">
      <li>Closed Stance</li><li>Hand Postioning</li><li>Picture Frame Positioning</li><li>Point of Origin</li>
    </ul>
    <h2 class="heading" style="left:550px;top:113px"><svg viewBox="0 0 16 18"><polygon points="8,0 15,9 8,18 1,9"/></svg>OFFENSE</h2>
    <ul class="list" style="left:572px;top:148px">
      <li>Back Fist</li><li>Body Punch</li><li>Round Kick</li><li>Side Kick</li>
    </ul>
    <h2 class="heading" style="left:300px;top:290px"><svg viewBox="0 0 16 18"><polygon points="8,0 15,9 8,18 1,9"/></svg>MOVEMENT</h2>
    <ul class="list" style="left:322px;top:330px"><li>Neutral Bounce</li></ul>
    <h2 class="heading" style="left:472px;top:296px"><svg viewBox="0 0 16 18"><polygon points="8,0 15,9 8,18 1,9"/></svg>DEFENCE / COUNTERS</h2>
    <ul class="list" style="left:550px;top:329px"><li>Wall Block</li><li>Push Checks</li></ul>
  </section>

  <svg class="ribbon" style="left:398px;top:436px" viewBox="0 0 252 49">
    <polygon points="0,0 252,0 232,24.5 252,49 0,49 20,24.5" fill="var(--ribbon)"/>
    <polygon points="6,4 246,4 228,24.5 246,45 6,45 24,24.5" fill="none" stroke="#d9c9c6" stroke-width="1" stroke-dasharray="3 2"/>
    <text x="126" y="35" text-anchor="middle">LEVEL TWO</text>
  </svg>

  <section class="level-two">
    <h2 class="heading" style="left:300px;top:505px"><svg viewBox="0 0 16 18"><polygon points="8,0 15,9 8,18 1,9"/></svg>CONCEPT</h2>
    <ul class="list" style="left:322px;top:540px">
      <li>Open Stance</li><li>Disturbing Rhythm</li><li>Technique Awareness</li>
    </ul>
    <h2 class="heading" style="left:459px;top:649px"><svg viewBox="0 0 16 18"><polygon points="8,0 15,9 8,18 1,9"/></svg>MOVEMENT</h2>
    <div class="rule" style="left:470px;top:676px;height:141px"></div>
    <ul class="list" style="left:484px;top:682px">
      <li>Engage</li><li>Disengage</li><li>Fakes</li><li>Single</li><li>Double</li>
    </ul>
    <h2 class="heading" style="left:300px;top:838px"><svg viewBox="0 0 16 18"><polygon points="8,0 15,9 8,18 1,9"/></svg>OFFENSE</h2>
    <ul class="list" style="left:322px;top:873px">
      <li>Push Drag Back Fist Wall</li><li>Push Drag Body Punch Wall</li><li>Step Drag Roundhouse</li><li>Step Drag Side Kick</li>
    </ul>
    <h2 class="heading" style="left:461px;top:1008px"><svg viewBox="0 0 16 18"><polygon points="8,0 15,9 8,18 1,9"/></svg>DEFENCE / COUNTERS</h2>
    <div class="rule" style="left:470px;top:1038px;height:82px"></div>
    <ul class="list" style="left:482px;top:1043px">
      <li>Body Punch</li><li>Closed Stance</li><li>Push Check Body Punch</li>
    </ul>
  </section>
</main>
</body>
</html>
```